Poster for our band

We need a logo and poster designing for us to send to the venues we are performing at. Our band is called "Quarry"
Can use different backgrounds to make poster look more Arty
We would like the poster to look contemporary, modern and unique. As many or as little pictures can be used that I will send.
We perform at Holiday Parks, Hotels etc so the Poster needs to look classy and sophisticated.Can be Portrait or Landscape. Poster could be Black and White or Colour
A very creative Logo
Could contain the following script somewhere on the poster.

Performing hits by- The Drifters Bay, Silver Lantern, Bright Oar, Darren Pollock, Moths of Varney, Gulls, Q9, Marble Poets and many more.

Poster needs our website address.
www.thebandquarry-example.co.uk

Poster needs our Agent Name and number

Represented by- RZK - 01632 960418

Target Market(s)

Holiday Parks
Hotels
Nightclubs
Bars

Industry/Entity Type

Colors
000000

Requirements
Must have
• Can be Portrait or Landscape. Poster could be Black and White or Colour
A very creative Logo

www.thebandquarry-example.co.uk

Nice to have
• Cool, Contemopoary, Modern design
Photos can be cut out or changed in anyway to make us look great.

```html
<!DOCTYPE html>
<html lang="en">
<head>
<meta charset="utf-8">
<title>Quarry – Band Poster</title>
<link href="https://fonts.googleapis.com/css2?family=Tinos:wght@400&display=swap" rel="stylesheet">
<style>
  :root {
    --ink: #000000;
    --paper: #ffffff;
    --gold: #c0924f;
    --gold-deep: #9a6c34;
    --grey-soft: #4a4a4a;
    --grey-mid: #2a2a2a;
  }
  html, body {
    margin: 0;
    padding: 0;
    background: var(--ink);
    overflow: hidden;
  }
  .poster {
    position: relative;
    width: 1200px;
    height: 784px;
    background: var(--ink);
    overflow: hidden;
    font-family: "Tinos", "Times New Roman", serif;
  }
  .band-photo {
    position: absolute;
    left: 0;
    top: 0;
    width: 1200px;
    height: 784px;
    background:
      radial-gradient(ellipse 150px 210px at 330px 210px, var(--grey-soft), transparent 75%),
      radial-gradient(ellipse 170px 230px at 600px 210px, #5a5a5a, transparent 75%),
      radial-gradient(ellipse 150px 210px at 870px 230px, var(--grey-soft), transparent 75%),
      radial-gradient(ellipse 520px 420px at 600px 560px, var(--grey-mid), transparent 80%),
      var(--ink);
  }
  .band-name {
    position: absolute;
    left: 0;
    width: 100%;
    top: 418px;
    margin: 0;
    text-align: center;
    font-size: 132px;
    font-weight: 400;
    line-height: 1;
    letter-spacing: 1px;
    color: var(--gold);
  }
  .setlist {
    position: absolute;
    left: 0;
    width: 100%;
    top: 618px;
    margin: 0;
    text-align: center;
    color: var(--paper);
    font-size: 24px;
    line-height: 42px;
    letter-spacing: 0.6px;
  }
  .website {
    position: absolute;
    left: 134px;
    top: 738px;
    color: var(--paper);
    font-size: 22px;
    letter-spacing: 0.4px;
  }
  .agent {
    position: absolute;
    left: 693px;
    top: 738px;
    color: var(--gold);
    font-size: 22px;
    letter-spacing: 0.4px;
  }
</style>
</head>
<body>
  <main class="poster">
    <div class="band-photo" role="img" aria-label="Black and white photograph of the three band members in suits against a black background"></div>
    <h1 class="band-name">Quarry</h1>
    <p class="setlist">Performing hits by- The Drifters Bay, Silver Lantern, Bright Oar, Darren Pollock,<br>Moths of Varney, Gulls, Q9, Marble Poets and many more.</p>
    <div class="website">www.thebandquarry-example.co.uk</div>
    <div class="agent">Represented by- RZK - 01632 960418</div>
  </main>
</body>
</html>
```